Kneadwell Haven Business Card Design

I want to create a very elegant and sophisticated two sided business card for my massage practice (www.kneadwellhaven-example.com). I have attached the logo and a PDF with some ideas down for the back of the card but I am open to suggestions. I will want to tie in a post card and flyer to the card later.
Similar colors to website would be great.
Target Market(s)
High end clientele, people looking for a sophisticated spa experience.
Industry/Entity Type
Massage
Contact Information for Business Card
Kneadwell Haven
7218 Larchmont Blvd S, Suite 305
Harborton, WA 98765
(555) 340-7816
www.kneadwellhaven-example.com

```html
<!DOCTYPE html>
<html lang="en">
<head>
<meta charset="utf-8">
<title>Kneadwell Haven – Business Card</title>
<link rel="stylesheet" href="https://fonts.googleapis.com/css2?family=Cinzel:wght@500&family=Montserrat:wght@400;500&display=swap">
<style>
  :root {
    --teal-deep: #11394a;
    --teal-sheen: #5d7e8b;
    --paper: #ffffff;
    --backdrop: #e4e6e7;
    --band-text: #eef3f5;
  }
  * { margin: 0; padding: 0; box-sizing: border-box; }
  html, body {
    width: 1200px;
    height: 900px;
    overflow: hidden;
    background: var(--backdrop);
  }
  .canvas {
    width: 1200px;
    height: 900px;
    display: flex;
    flex-direction: column;
    align-items: center;
    justify-content: center;
    gap: 40px;
  }
  .card {
    width: 630px;
    height: 360px;
    position: relative;
    overflow: hidden;
    box-shadow: 0 6px 18px rgba(0, 0, 0, 0.18);
  }
  .card-back {
    background: var(--teal-deep);
    display: flex;
    align-items: center;
    justify-content: center;
  }
  .card-front {
    background: var(--paper);
    display: flex;
    flex-direction: column;
  }
  .brand-name {
    font-family: "Cinzel", serif;
    font-weight: 500;
    font-size: 38px;
    letter-spacing: 1px;
    white-space: nowrap;
  }
  .card-back .brand-name { color: var(--teal-sheen); }
  .card-front .brand-area {
    flex: 1;
    display: flex;
    align-items: center;
    justify-content: center;
  }
  .card-front .brand-name { color: var(--teal-deep); }
  .contact-band {
    height: 104px;
    background: var(--teal-deep);
    color: var(--band-text);
    font-family: "Montserrat", sans-serif;
    font-weight: 400;
    font-size: 17px;
    letter-spacing: 0.6px;
    line-height: 1.6;
    display: flex;
    flex-direction: column;
    align-items: center;
    justify-content: center;
    text-align: center;
  }
  .contact-line { white-space: nowrap; }
  .contact-band .divider { margin: 0 6px; }
</style>
</head>
<body>
  <main class="canvas">
    <section class="card card-back" aria-label="Card back">
      <p class="brand-name">Kneadwell Haven</p>
    </section>

    <section class="card card-front" aria-label="Card front">
      <div class="brand-area">
        <p class="brand-name">Kneadwell Haven</p>
      </div>
      <div class="contact-band">
        <p class="contact-line">(555) 340-7816<span class="divider">|</span>www.kneadwellhaven-example.com</p>
        <p class="contact-line">7218 Larchmont Blvd S, Suite 305 Harborton, WA 98765</p>
      </div>
    </section>
  </main>
</body>
</html>
```